July 4th Postcard to existing clients

5x7 postcard wishing our clients happy 4th of July. Card should read on the back "Thank You For Being A Valued Client!. Stay Safe And Enjoy Your Independence Day Celebrations!"

Patriotic theme with fireworks is ideal. We are a law firm so should still have a feel of professionalism while still being fun since it is for a fun holiday.

```html
<!DOCTYPE html>
<html lang="en">
<head>
<meta charset="utf-8">
<title>Halden Law – Independence Day Postcard</title>
<link rel="stylesheet" href="https://fonts.googleapis.com/css2?family=Montserrat:wght@400;800&family=Oswald:wght@300&family=Cormorant+Garamond:ital,wght@1,500&family=Caveat:wght@700&family=Roboto+Slab:wght@300;400&family=Lato:wght@400;700&display=swap">
<style>
  :root {
    --navy: #2c4a7e;
    --navy-deep: #1f3a6b;
    --lavender: #a9acce;
    --lavender-soft: #c4c6df;
    --ink: #4a4a4c;
    --band: #3b3b3d;
    --paper: #ffffff;
    --backdrop: #e8e6e3;
  }
  html, body {
    margin: 0;
    width: 1200px;
    height: 1200px;
    overflow: hidden;
    background: var(--backdrop);
  }
  .canvas { position: relative; width: 1200px; height: 1200px; }
  .card {
    position: absolute;
    background: var(--paper);
    box-shadow: 0 4px 14px rgba(0,0,0,.18);
  }
  .card svg { display: block; width: 100%; height: 100%; }
  .card--front { left: 35px; top: 292px; width: 440px; height: 616px; }
  .card--back  { left: 505px; top: 364px; width: 660px; height: 472px; }

  .headline-happy { font-family: "Montserrat", sans-serif; font-weight: 800; fill: var(--navy); }
  .headline-date  { font-family: "Oswald", sans-serif; font-weight: 300; fill: var(--ink); }
  .firm-name      { font-family: "Montserrat", sans-serif; font-weight: 400; fill: var(--ink); letter-spacing: 1px; }
  .tagline        { font-family: "Cormorant Garamond", serif; font-style: italic; font-weight: 500; fill: var(--navy); }
  .thanks-script  { font-family: "Caveat", cursive; font-weight: 700; }
  .greeting       { font-family: "Roboto Slab", serif; font-weight: 300; fill: #2e2e33; }
  .greeting--accent { font-weight: 400; fill: var(--navy); }
  .band-text      { font-family: "Lato", sans-serif; fill: #ffffff; }
</style>
</head>
<body>
<main class="canvas">

  <!-- Front of postcard -->
  <section class="card card--front" aria-label="Postcard front">
    <svg viewBox="0 0 500 700" xmlns="http://www.w3.org/2000/svg">
      <defs>
        <linearGradient id="libraryTones" x1="0" y1="0" x2="1" y2="1">
          <stop offset="0" stop-color="#7a3a3a"/>
          <stop offset=".5" stop-color="#b98a5e"/>
          <stop offset="1" stop-color="#5b2c32"/>
        </linearGradient>
        <linearGradient id="meetingTones" x1="0" y1="0" x2="1" y2="1">
          <stop offset="0" stop-color="#d8cbbd"/>
          <stop offset=".55" stop-color="#b89b86"/>
          <stop offset="1" stop-color="#3f3f46"/>
        </linearGradient>
      </defs>

      <g class="greeting-frame">
        <rect x="71" y="41" width="358" height="162" fill="none" stroke="var(--navy)" stroke-width="1.5"/>
        <text class="headline-happy" x="250" y="103" text-anchor="middle" font-size="56">HAPPY</text>
        <text class="headline-date" x="250" y="183" text-anchor="middle" font-size="74">4<tspan font-size="40" dy="-30">th</tspan><tspan dy="30"> of JULY</tspan></text>
      </g>

      <g class="decor-shapes">
        <polygon points="355,238 438,238 475,305 392,305" fill="var(--lavender)" opacity=".75"/>
        <polygon points="218,443 300,443 330,505 250,505" fill="var(--lavender)" opacity=".75"/>
        <polygon points="410,530 499,530 499,570 430,570" fill="var(--lavender)" opacity=".75"/>
        <polygon points="443,562 499,562 499,634 478,634" fill="var(--lavender-soft)" opacity=".9"/>
      </g>

      <polygon class="photo" role="img" aria-label="Photo: handshake over a desk with scales of justice in front of law books"
        points="220,272 430,272 499,410 499,425 311,425" fill="url(#libraryTones)"/>
      <polygon points="430,282 441,282 499,398 499,420" fill="var(--navy)"/>
      <rect x="310" y="430" width="189" height="9" fill="var(--navy)"/>

      <polygon class="photo" role="img" aria-label="Photo: young couple shaking hands with a lawyer at a meeting"
        points="0,475 305,475 398,698 0,698" fill="url(#meetingTones)"/>
      <polygon points="313,490 322,490 405,682 396,682" fill="var(--navy)"/>

      <g class="brand">
        <rect x="118" y="318" width="28" height="28" fill="var(--lavender)"/>
        <text class="firm-name" x="132" y="387" text-anchor="middle" font-size="26">HALDEN LAW</text>
        <text class="tagline" x="126" y="413" text-anchor="middle" font-size="17">It’s about taking responsibility</text>
      </g>
    </svg>
  </section>

  <!-- Back of postcard -->
  <section class="card card--back" aria-label="Postcard back">
    <svg viewBox="0 0 700 500" xmlns="http://www.w3.org/2000/svg">
      <defs>
        <linearGradient id="justiceTones" x1="0" y1="0" x2="1" y2="1">
          <stop offset="0" stop-color="#e6e3ec"/>
          <stop offset=".45" stop-color="#b3aec2"/>
          <stop offset=".8" stop-color="#6d6a7c"/>
          <stop offset="1" stop-color="#3b3a48"/>
        </linearGradient>
      </defs>

      <polygon class="photo" role="img" aria-label="Photo: statue of Lady Justice holding scales in a law library"
        points="0,0 402,0 348,328 0,328" fill="url(#justiceTones)"/>
      <polygon points="406,18 421,18 361,368 346,368" fill="var(--navy)"/>

      <g class="message">
        <text class="thanks-script" x="25" y="72" font-size="40" fill="var(--navy)">Thank You</text>
        <text class="thanks-script" x="77" y="104" font-size="22" fill="#333">For Being</text>
        <text class="thanks-script" x="40" y="134" font-size="22" fill="#333">A Valued Client!.</text>
        <text class="greeting" x="117" y="182" text-anchor="middle" font-size="17">Stay Safe</text>
        <text class="greeting" x="117" y="204" text-anchor="middle" font-size="17">&amp; Enjoy Your</text>
        <text class="greeting" x="117" y="226" text-anchor="middle" font-size="17">Independence Day</text>
        <text class="greeting greeting--accent" x="117" y="247" text-anchor="middle" font-size="17">CELEBRATIONS!</text>
      </g>

      <g class="contact-band">
        <polygon points="0,331 347,331 335,419 0,419" fill="var(--band)"/>
        <text class="band-text" x="32" y="358" font-size="11"><tspan font-weight="700">HALDEN</tspan> LAW</text>
        <path d="M22 373 l4 -4 l4 4 v4 h-8 z" fill="none" stroke="#cfcfd2" stroke-width="1"/>
        <text class="band-text" x="33" y="379" font-size="10.5" font-weight="700">1480 North Maple Avenue</text>
        <text class="band-text" x="33" y="392" font-size="10.5" font-weight="700">Riverton, Ohio 44120</text>
        <line x1="183" y1="371" x2="183" y2="409" stroke="#ffffff" stroke-width="1"/>
        <text class="band-text" x="193" y="379" font-size="10.5"><tspan font-weight="700">Telephone:</tspan> (555) 210-4477</text>
        <text class="band-text" x="193" y="392" font-size="10.5"><tspan font-weight="700">Toll Free:</tspan> 1-800-555-0192</text>
        <text class="band-text" x="193" y="405" font-size="10.5"><tspan font-weight="700">Fax:</tspan> (555) 210-4480</text>
      </g>

      <g class="brand">
        <rect x="470" y="38" width="14" height="14" fill="var(--lavender)"/>
        <text class="firm-name" x="430" y="79" font-size="15">HALDEN LAW</text>
      </g>

      <rect class="stamp-box" x="599" y="27" width="67" height="72" fill="none" stroke="#333" stroke-width="1.2"/>

      <g class="address-lines" stroke="#333" stroke-width="2.5">
        <line x1="445" y1="300" x2="674" y2="300"/>
        <line x1="445" y1="330" x2="674" y2="330"/>
        <line x1="445" y1="360" x2="674" y2="360"/>
      </g>
    </svg>
  </section>

</main>
</body>
</html>
```